BHSC Business cards

We are an established dental practice that is looking for new business cards to match our new logo. We are looking for something unique and sophisticated.
BRIEF: Colours are black, silver and white. Include the company name, logo (including “Pelwick Heath Dental Care”) and phone number “03 9415 2876”.
Front - Include the company name, logo (including “Pelwick Heath Dental Care”) and phone number “03 9415 2876”.
Back - Include the company name,  “Pelwick Heath Dental Care”, phone number “03 9415 2876”. address "64A Tindle Street, Pelwick Heath, Vic 3187", "Email reception@pelwickheathdentalcare.com.au", the Dentist Name " Dr ................................"  Your next appointment "Day, date and time(am/pm)".  3 lines for 3 appointments please, and at the bottom "IF UNABLE TO KEEP THIS APPOINTMENT 48 HOURS NOTICE IS REQUIRED."
Try and be creative and different with the design, i've added an image for inspiration

Target Market(s)
ALL in need of dental
Industry/Entity Type
Dental Clinic
Look and feel
Each slider illustrates characteristics of the customer's brand and the style your logo design should communicate.

```html
<!DOCTYPE html>
<html lang="en">
<head>
<meta charset="utf-8">
<title>Pelwick Heath Dental Care – Business Cards</title>
<link rel="stylesheet" href="https://fonts.googleapis.com/css2?family=Poppins:wght@300;400;500;600&display=swap">
<style>
  :root {
    --page: #8e8e8e;
    --paper: #ffffff;
    --ink: #231f20;
    --band: #2b2627;
    --card-dark: #2a2526;
    --card-dark-2: #1f1b1c;
    --silver: #a99ea0;
    --dots: #6d6869;
  }
  * { box-sizing: border-box; margin: 0; padding: 0; }
  html, body { width: 1200px; height: 1200px; overflow: hidden; }
  body {
    background: var(--page);
    font-family: "Poppins", sans-serif;
    color: var(--ink);
    position: relative;
  }
  .card {
    position: absolute;
    left: 262px;
    width: 685px;
    height: 390px;
    border-radius: 20px;
    overflow: hidden;
  }
  /* Appointment side */
  .card--appointment { top: 165px; background: var(--paper); }
  .brand {
    position: absolute; top: 28px; left: 0; right: 0; text-align: center;
  }
  .brand__name {
    font-weight: 600; font-size: 25px; letter-spacing: 1.5px; text-transform: uppercase; line-height: 1.1;
  }
  .brand__phone {
    font-weight: 500; font-size: 15px; letter-spacing: 3px; margin-top: 4px;
  }
  .form { position: absolute; left: 71px; right: 55px; top: 95px; font-size: 15px; }
  .row { display: flex; align-items: flex-end; height: 41px; }
  .row:first-child { height: 26px; margin-bottom: 4px; }
  .label { font-weight: 600; white-space: nowrap; }
  .fill { flex: 1; border-bottom: 1.5px dotted var(--dots); margin: 0 4px 5px; }
  .fill--day { flex: 0 0 170px; }
  .fill--date { flex: 0 0 150px; }
  .fill--time { flex: 0 0 80px; }
  .soft { font-weight: 400; white-space: nowrap; }
  .small { font-size: 13px; }
  .notice {
    position: absolute; top: 263px; left: 0; right: 0; text-align: center;
    font-size: 12.5px; letter-spacing: 2.3px; font-weight: 400;
  }
  .band {
    position: absolute; left: 0; right: 0; top: 307px; height: 66px; background: var(--band);
    color: #fff; display: flex; align-items: center; justify-content: space-between; padding: 0 95px 0 72px;
  }
  .contacts { list-style: none; font-size: 13.5px; font-weight: 400; line-height: 17px; }
  .contacts li { display: flex; align-items: center; gap: 7px; }
  .contacts svg { width: 10px; height: 10px; fill: #fff; flex: none; }
  .mark-circle { width: 64px; height: 64px; border-radius: 50%; border: 2.5px solid #fff; background: var(--band); }
  /* Brand side */
  .card--brand {
    top: 653px;
    background: linear-gradient(160deg, var(--card-dark) 0%, var(--card-dark-2) 100%);
    display: flex; align-items: center; justify-content: center; gap: 20px;
  }
  .card--brand .mark-circle { width: 80px; height: 80px; border: 3px solid var(--silver); background: transparent; }
  .card--brand .brand__name { color: var(--silver); font-size: 27px; }
  .card--brand .brand__phone { color: var(--silver); text-align: left; font-size: 16px; }
</style>
</head>
<body>
  <section class="card card--appointment">
    <header class="brand">
      <div class="brand__name">Pelwick Heath Dental Care</div>
      <div class="brand__phone">03 9415 2876</div>
    </header>
    <div class="form">
      <div class="row"><span class="label">DR</span><span class="fill"></span><span class="soft">Your next appointment</span></div>
      <div class="row"><span class="label">Day</span><span class="fill fill--day"></span><span class="label">Date</span><span class="fill fill--date"></span><span class="soft">at</span><span class="fill fill--time"></span><span class="soft small">AM/PM</span></div>
      <div class="row"><span class="label">Day</span><span class="fill fill--day"></span><span class="label">Date</span><span class="fill fill--date"></span><span class="soft">at</span><span class="fill fill--time"></span><span class="soft small">AM/PM</span></div>
      <div class="row"><span class="label">Day</span><span class="fill fill--day"></span><span class="label">Date</span><span class="fill fill--date"></span><span class="soft">at</span><span class="fill fill--time"></span><span class="soft small">AM/PM</span></div>
    </div>
    <p class="notice">IF UNABLE TO KEEP THIS APPOINTMENT 48 HOURS NOTICE IS REQUIRED.</p>
    <footer class="band">
      <ul class="contacts">
        <li><svg viewBox="0 0 10 10"><path d="M5 0a3.5 3.5 0 0 0-3.5 3.5C1.5 6 5 10 5 10s3.5-4 3.5-6.5A3.5 3.5 0 0 0 5 0zm0 5a1.4 1.4 0 1 1 0-2.8A1.4 1.4 0 0 1 5 5z"/></svg>64A Tindle Street, Pelwick Heath, Vic 3187</li>
        <li><svg viewBox="0 0 10 10"><path d="M0 2h10v6H0z M0 2l5 3.5L10 2" stroke="#2b2627" stroke-width="0.8"/></svg>reception@pelwickheathdentalcare.com.au</li>
        <li><svg viewBox="0 0 10 10"><circle cx="5" cy="5" r="4.6"/><path d="M0.6 5h8.8M5 0.4v9.2" stroke="#2b2627" stroke-width="0.8"/></svg>www.pelwickheathdentalcare.com.au</li>
      </ul>
      <div class="mark-circle"></div>
    </footer>
  </section>

  <section class="card card--brand">
    <div class="mark-circle"></div>
    <div>
      <div class="brand__name">Pelwick Heath Dental Care</div>
      <div class="brand__phone">03 9415 2876</div>
    </div>
  </section>
</body>
</html>
```